business card for real estate company
Coastway Summit Realty
Simple
Dimitri Lavrentis
Broker / Owner
118 Alder Lane
Larkhaven, CW 02417
dimitri@coastsummitrealty.com
www.coastsummitrealty.com
clean professional look that people wont have a hard time reading. Thank you in advance for your designs.

```html
<!DOCTYPE html>
<html lang="en">
<head>
<meta charset="utf-8">
<title>Coastway Summit Realty – Business Card</title>
<link rel="stylesheet" href="https://fonts.googleapis.com/css2?family=Cinzel:wght@400;600&display=swap">
<style>
  :root {
    --backdrop: #e9e6e1;
    --card: #ffffff;
    --brand-blue: #1f3f9a;
    --ink-blue: #233a7a;
    --ink-grey: #4a4d55;
    --band-dark: #3a3c42;
    --band-light: #4f73d6;
    --rule: #8a8f99;
  }
  * { box-sizing: border-box; margin: 0; padding: 0; }
  html, body {
    width: 1200px; height: 914px; overflow: hidden;
    background: var(--backdrop);
    font-family: "Cinzel", "Times New Roman", serif;
  }
  .business-card {
    position: absolute; left: 100px; top: 171px;
    width: 1000px; height: 572px;
    background: var(--card);
    box-shadow: 0 10px 30px rgba(0,0,0,0.18);
    overflow: hidden;
  }
  .brand {
    position: absolute; left: 300px; top: 104px;
    display: flex; align-items: center; gap: 18px;
  }
  .brand-square {
    width: 46px; height: 46px; background: var(--brand-blue); flex: none;
  }
  .brand-name {
    font-weight: 600; font-size: 34px; letter-spacing: 1px;
    color: var(--brand-blue); line-height: 1.1; white-space: nowrap;
  }
  .agent {
    position: absolute; right: 540px; top: 250px;
    text-align: right; color: var(--ink-grey);
    font-size: 20px; line-height: 1.45; white-space: nowrap;
  }
  .agent-name {
    color: var(--ink-blue); font-size: 26px; font-weight: 600;
    margin-bottom: 2px;
  }
  .divider {
    position: absolute; left: 478px; top: 258px;
    width: 1.5px; height: 150px; background: var(--rule);
  }
  .contact-list {
    position: absolute; left: 498px; top: 256px;
    list-style: none; color: var(--ink-grey); font-size: 19px;
  }
  .contact-list li {
    display: flex; align-items: center; gap: 12px; height: 37px; white-space: nowrap;
  }
  .contact-icon { width: 22px; height: 22px; flex: none; }
  .bottom-bands {
    position: absolute; left: 0; bottom: 0; width: 1000px; height: 130px;
  }
  .band-blue { fill: var(--brand-blue); }
  .band-highlight { fill: var(--band-light); }
  .band-dark { fill: var(--band-dark); }
</style>
</head>
<body>
  <div class="business-card">
    <div class="brand">
      <span class="brand-square"></span>
      <span class="brand-name">Coastway Summit Realty</span>
    </div>

    <div class="agent">
      <p class="agent-name">Dimitri Lavrentis</p>
      <p>Broker / Owner</p>
      <p>118 Alder Lane</p>
      <p>Larkhaven, CW 02417</p>
    </div>

    <div class="divider"></div>

    <ul class="contact-list">
      <li>
        <svg class="contact-icon" viewBox="0 0 22 22"><circle cx="11" cy="11" r="11" fill="#1f3f9a"/><path d="M7.5 5.5l2 .3.8 2.6-1.3 1a6 6 0 0 0 3 3l1-1.3 2.6.8.3 2a1.5 1.5 0 0 1-1.6 1.3A9 9 0 0 1 6 7.1 1.5 1.5 0 0 1 7.5 5.5z" fill="#fff"/></svg>
        <span>(781) 555-0148</span>
      </li>
      <li>
        <svg class="contact-icon" viewBox="0 0 22 22"><circle cx="11" cy="11" r="11" fill="#1f3f9a"/><rect x="7.5" y="4.5" width="7" height="13" rx="1.3" fill="#fff"/><rect x="8.7" y="6" width="4.6" height="8.5" fill="#1f3f9a"/></svg>
        <span>(781) 555-0192</span>
      </li>
      <li>
        <svg class="contact-icon" viewBox="0 0 22 22"><circle cx="11" cy="11" r="11" fill="#1f3f9a"/><rect x="5" y="7" width="12" height="8.5" fill="#fff"/><path d="M5 7l6 5 6-5" fill="none" stroke="#1f3f9a" stroke-width="1.2"/></svg>
        <span>dimitri@coastsummitrealty.com</span>
      </li>
      <li>
        <svg class="contact-icon" viewBox="0 0 22 22"><circle cx="11" cy="11" r="11" fill="#1f3f9a"/><g fill="none" stroke="#fff" stroke-width="1.2"><circle cx="11" cy="11" r="6"/><ellipse cx="11" cy="11" rx="2.6" ry="6"/><path d="M5 11h12"/></g></svg>
        <span>www.coastsummitrealty.com</span>
      </li>
    </ul>

    <svg class="bottom-bands" viewBox="0 0 1000 130" aria-hidden="true">
      <polygon class="band-blue" points="0,20 600,20 660,82 0,82"/>
      <polygon class="band-highlight" points="0,20 600,20 606,26 0,26"/>
      <polygon class="band-dark" points="672,58 1000,58 1000,104 716,104"/>
    </svg>
  </div>
</body>
</html>
```